web page layout, style , color, font & flow design

We are developing a single page application. The SPA (single page application) will display natural gas pipeline flow data once the customer logs on. The customer has a choice of the region, the pipeline, the zone on the pipeline, whether the point is a delivery point or receipt point and the state the pipeline flows through.
we have jumpstarted the project and are attaching a pdf of the same.

we are using mockingbird for the wireframe. any designer is free to use this tool to make changes.

A mockingbird wireframe link is added below. you are free to use it and to make changes. please save the changed wireframe in a different name

we are looking for inputs on layout, style , color, font & flow.

A logo jpg file has also been attached.

Target Market(s)

this single web page is going to be used by natural gas traders and schedulers day in and day out. the application is more of business to business corporate application.

Industry/Entity Type

Delivery

Requirements
Must have
• layout ,flow, size, color, font , ease of use.

```html
<!DOCTYPE html>
<html lang="en">
<head>
<meta charset="utf-8">
<title>Wholesale NG Supply Analysis</title>
<link rel="stylesheet" href="https://fonts.googleapis.com/css2?family=Open+Sans:ital,wght@0,400;0,600;0,700;1,600&display=swap">
<style>
:root{
  --page-top:#2b313b;
  --page-bottom:#4f5966;
  --header-bg:#ffffff;
  --green:#5ba50f;
  --orange:#e9845b;
  --blue:#2f8ce2;
  --sidebar:#23272d;
  --sidebar-line:#2d3238;
  --sidebar-text:#b9bec4;
  --content:#e4e7ea;
  --control:#25282d;
  --table-bg:#f7f7f7;
  --table-head:#eeeeee;
  --table-line:#d9dbdd;
  --text:#555a60;
  --muted:#7d8186;
  --avatar:#8b9aa8;
}
*{margin:0;padding:0;box-sizing:border-box}
html,body{width:1200px;height:785px;overflow:hidden}
body{
  font-family:"Open Sans",sans-serif;
  background:radial-gradient(ellipse at 50% 100%,var(--page-bottom),var(--page-top) 75%);
  position:relative;color:var(--text);
}
.app{position:absolute;left:98px;top:0;width:1004px;height:728px;background:var(--content)}
.topbar{height:47px;background:var(--header-bg);position:relative}
.brand{position:absolute;left:12px;top:11px;display:flex;align-items:center;gap:10px}
.brand-dot{width:24px;height:24px;border-radius:50%;background:var(--green)}
.brand-name{font-size:14px;font-style:italic;font-weight:600;color:#333}
.tools{position:absolute;left:272px;top:16px;display:flex;gap:10px}
.user{position:absolute;right:14px;top:7px;display:flex;align-items:center;gap:10px;font-size:14px;color:#333}
.avatar{width:32px;height:32px;border-radius:50%;background:linear-gradient(#6b7d8e,var(--avatar))}
.tabs{position:absolute;top:47px;left:4px;display:flex;gap:7px}
.tab{width:160px;height:43px;display:flex;align-items:center;justify-content:center;color:#fff;font-weight:600;font-size:13.5px}
.tab.green{background:var(--green)}.tab.orange{background:var(--orange)}.tab.blue{background:var(--blue)}
.tab.active{border-top:3px solid #1f2326}
.sidebar{position:absolute;left:0;top:90px;width:243px;height:638px;background:var(--sidebar)}
.pipe{height:36px;display:flex;align-items:center;padding-left:30px;font-size:12.5px;color:var(--sidebar-text);border-bottom:1px solid var(--sidebar-line)}
.pipe::before{content:"";width:5px;height:5px;border-left:1px solid currentColor;border-bottom:1px solid currentColor;transform:rotate(45deg);margin-right:10px}
.pipe.current{color:var(--green)}
.filters{position:absolute;left:273px;top:116px;display:flex;gap:4px}
.select{height:29px;background:var(--control);border-radius:2px;color:#fff;font-size:11px;font-weight:600;display:flex;align-items:center;gap:6px;padding:0 8px}
.select .caret{width:0;height:0;border-left:5px solid transparent;border-right:5px solid transparent;border-top:6px solid #fff;margin-left:auto}
.captions{position:absolute;top:149px;font-size:10px;font-style:italic;color:var(--muted)}
.updates{position:absolute;left:828px;top:116px;width:131px}
.menu{position:absolute;left:816px;top:151px;width:158px;background:var(--control);padding:4px 0;z-index:2}
.menu div{height:30px;line-height:30px;padding-left:13px;color:#fff;font-size:12.5px}
.menu .on{background:var(--green)}
.grid{position:absolute;left:273px;top:184px;width:701px;border-collapse:collapse;background:var(--table-bg);font-size:11px;text-align:center;box-shadow:0 1px 2px rgba(0,0,0,.1)}
.grid th{height:53px;font-weight:400;font-size:13px;color:#444;background:var(--table-head);border:1px solid var(--table-line)}
.grid td{height:42.6px;border:1px solid var(--table-line)}
.pager{position:absolute;left:696px;top:689px;display:flex;gap:5px;align-items:center}
.pager span{min-width:21px;height:21px;padding:0 3px;background:#1e2125;color:#fff;font-size:10.5px;font-weight:700;display:flex;align-items:center;justify-content:center;border-radius:2px}
.pager .active{background:#4a5663}
.pager .gap{background:none;color:#888}
.footer{position:absolute;top:747px;width:100%;text-align:center;color:#fff;font-size:11px}
</style>
</head>
<body>
<div class="app">
  <header class="topbar">
    <div class="brand"><span class="brand-dot"></span><span class="brand-name">Wholesale NG Supply Analysis</span></div>
    <div class="tools">
      <svg width="13" height="13" viewBox="0 0 13 13"><circle cx="5.5" cy="5.5" r="4" fill="none" stroke="#bbb" stroke-width="1.8"/><line x1="8.5" y1="8.5" x2="12" y2="12" stroke="#bbb" stroke-width="2"/></svg>
      <svg width="13" height="13" viewBox="0 0 13 13"><path d="M11 6.5A4.5 4.5 0 1 1 9.5 3" fill="none" stroke="#bbb" stroke-width="1.8"/><path d="M8 1h3.5v3.5z" fill="#bbb"/></svg>
    </div>
    <div class="user"><span class="avatar" role="img" aria-label="User profile photo"></span>Morgan Hale Re
      <svg width="14" height="14" viewBox="0 0 14 14"><circle cx="7" cy="7" r="4.5" fill="none" stroke="#777" stroke-width="3" stroke-dasharray="2.2 1.3"/><circle cx="7" cy="7" r="2.5" fill="none" stroke="#777" stroke-width="1.5"/></svg>
    </div>
  </header>
  <nav class="tabs">
    <div class="tab green active">NORTHEAST</div><div class="tab orange">MIDWEST</div><div class="tab blue">SOUTHEAST</div>
    <div class="tab green">SOUTHWEST</div><div class="tab orange">CENTRAL</div><div class="tab blue">WEST</div>
  </nav>
  <aside class="sidebar">
    <div class="pipe current">Alder Creek</div><div class="pipe">NRT</div><div class="pipe">Dorset</div>
    <div class="pipe">Coastal Shore NG</div><div class="pipe">East Ridge NG</div><div class="pipe">Summit Gas</div>
    <div class="pipe">Equiline Inc</div><div class="pipe">Granite Ridge Gas</div><div class="pipe">Iron Lake</div>
    <div class="pipe">Harbor &amp; North East</div><div class="pipe">Meridian Pipeline</div><div class="pipe">National Heat Gas Supply Corp</div>
    <div class="pipe">Portside NG</div><div class="pipe">St. Clair Gas</div><div class="pipe">Valley Gas</div>
    <div class="pipe">Texline</div><div class="pipe">Transline</div>
  </aside>
  <div class="filters">
    <div class="select" style="width:131px"><svg width="10" height="10" viewBox="0 0 10 10"><path d="M10 0L0 4.5 4.5 5.5 5.5 10z" fill="#bbb"/></svg>LOCATION TYPE<span class="caret"></span></div>
    <div class="select" style="width:130px"><svg width="11" height="8" viewBox="0 0 11 8"><ellipse cx="5.5" cy="4" rx="5" ry="3.5" fill="#bbb"/><circle cx="5.5" cy="4" r="1.6" fill="#25282d"/></svg>STATES<span class="caret"></span></div>
    <div class="select" style="width:130px"><svg width="10" height="11" viewBox="0 0 10 11"><path d="M5 1v9M2 3h6M1 7q4 5 8 0" fill="none" stroke="#bbb" stroke-width="1.4"/></svg>ZONES<span class="caret" style="margin-left:4px;margin-right:auto"></span></div>
  </div>
  <div class="captions" style="left:287px">Receipt, Delivery, Storage</div>
  <div class="captions" style="left:455px">Interstate Pipeline</div>
  <div class="captions" style="left:606px">Pipeline Zones</div>
  <div class="select updates"><svg width="10" height="10" viewBox="0 0 10 10"><path d="M8.5 5A3.5 3.5 0 1 1 7 2.2" fill="none" stroke="#bbb" stroke-width="1.4"/></svg>GAS UPDATES<span class="caret"></span></div>
  <div class="menu"><div>Timely</div><div class="on">Evening</div><div>Interday1</div><div>Interday2</div></div>
  <table class="grid">
    <tr><th style="width:90px">Gasday</th><th style="width:90px">Location</th><th style="width:111px">Location Name</th><th style="width:82px">Flow_Ind</th><th style="width:74px">Loc_Desc</th><th style="width:84px">Op_cap</th><th style="width:84px">Sch_cap</th><th style="width:86px">Av_cap</th></tr>
    <tr><td>Item 3</td><td>Item 3</td><td>DORSET..</td><td>Delivery</td><td>DPQ</td><td>5,47,181</td><td>721</td><td>4180</td></tr>
    <tr><td>Item 5</td><td>Item 2</td><td>CORNWALL..</td><td>Delivery</td><td>DPQ</td><td>4,41,824</td><td>805</td><td>4805</td></tr>
    <tr><td>Item 7</td><td>Item 1</td><td>INDIANA..</td><td>Delivery</td><td>DPQ</td><td>5,402</td><td>402</td><td>4020</td></tr>
    <tr><td>Item 8</td><td>Item 6</td><td>INDIANA..</td><td>Delivery</td><td>DPQ</td><td>63,989</td><td>3,989</td><td>989</td></tr>
    <tr><td>Item 11</td><td>Item 8</td><td>EQUILINE..</td><td>Delivery</td><td>DPQ</td><td>5,402</td><td>2</td><td>200</td></tr>
    <tr><td>Item 15</td><td>Item 9</td><td>NATIONAL..</td><td>Delivery</td><td>DPQ</td><td>55,588</td><td>788</td><td>88</td></tr>
    <tr><td>Item 17</td><td>Item 10</td><td>NATIONAL..</td><td>Delivery</td><td>DPQ</td><td>24,228</td><td>4,228</td><td>4,228</td></tr>
    <tr><td>Item 15</td><td>Item 9</td><td>NATIONAL..</td><td>Delivery</td><td>DPQ</td><td>55,588</td><td>788</td><td>88</td></tr>
    <tr><td>Item 17</td><td>Item 10</td><td>NATIONAL..</td><td>Delivery</td><td>DPQ</td><td>24,228</td><td>4,228</td><td>4,228</td></tr>
    <tr><td>Item 15</td><td>Item 9</td><td>NATIONAL..</td><td>Delivery</td><td>DPQ</td><td>55,588</td><td>788</td><td>88</td></tr>
  </table>
  <div class="pager">
    <span>&lsaquo;</span><span>1</span><span class="active">2</span><span>3</span><span>4</span><span>5</span><span class="gap">...</span><span>10</span><span>20</span><span>30</span><span>&rsaquo;</span>
  </div>
</div>
<div class="footer">© 2014 Wholesale NG Supply Analysis. All Rights Reserved</div>
</body>
</html>
```